ASSET BASED PROGRAM FLIER

Need flier to market hard money loan products offered HARD MONEY FIX & FLIP PROGRAMS

We offer a variety of loan programs Some program highlights include......

1) No Minimum Credit Score
2) 3-5 Day Close
3) Up to 100% of Purchase & Rehab
4) Rates as Low as 7%
5) Loans Offered Nationwide

Contact us today for more information at (800) 416-2905 x42 or email us at mvoss@brightlanelending.com NMLS #781536 www.brightlanelending.com

```html
<!DOCTYPE html>
<html lang="en">
<head>
<meta charset="utf-8">
<title>Hard Money Fix &amp; Flip Programs Flier</title>
<link rel="stylesheet" href="https://fonts.googleapis.com/css2?family=Cinzel:wght@400;700;900&family=Lato:wght@400;700&family=Roboto+Condensed:wght@400;700&display=swap">
<style>
  :root {
    --page-bg: #e9e9e9;
    --paper: #ffffff;
    --brand-blue: #0f5aa8;
    --deep-blue: #0a4d96;
    --gold: #a99a2c;
    --ink: #2b2b2b;
    --text-grey: #3d3d3d;
  }
  html, body {
    margin: 0;
    width: 1200px;
    height: 1200px;
    overflow: hidden;
    background: var(--page-bg);
  }
  .flier {
    position: absolute;
    left: 193px;
    top: 30px;
    width: 814px;
    height: 1140px;
    box-shadow: 0 6px 18px rgba(0,0,0,0.25);
  }
  .flier svg { display: block; width: 100%; height: 100%; }
  .headline { font-family: "Cinzel", serif; fill: var(--brand-blue); font-size: 71px; font-weight: 400; }
  .headline-strong { font-family: "Cinzel", serif; fill: var(--ink); font-size: 64px; font-weight: 900; }
  .intro { font-family: "Roboto Condensed", sans-serif; fill: var(--text-grey); font-size: 24px; }
  .intro-strong { font-family: "Roboto Condensed", sans-serif; fill: var(--brand-blue); font-size: 24px; font-weight: 700; }
  .highlight { font-family: "Lato", sans-serif; fill: var(--text-grey); font-size: 20px; }
  .highlight-accent { fill: var(--brand-blue); font-weight: 700; }
  .brand-name { font-family: "Lato", sans-serif; fill: var(--brand-blue); font-size: 26px; font-weight: 700; }
  .photo-label { font-family: "Lato", sans-serif; fill: #ffffff; font-size: 17px; }
  .contact-main { font-family: "Lato", sans-serif; fill: #ffffff; font-size: 26px; }
  .contact { font-family: "Lato", sans-serif; fill: #ffffff; font-size: 16px; }
</style>
</head>
<body>
<div class="flier">
<svg viewBox="0 0 928 1300" xmlns="http://www.w3.org/2000/svg">
  <defs>
    <linearGradient id="room-tone" x1="0" y1="0" x2="1" y2="1">
      <stop offset="0" stop-color="#eef0ef"/>
      <stop offset="0.55" stop-color="#d9dcd8"/>
      <stop offset="1" stop-color="#b7b5ad"/>
    </linearGradient>
    <linearGradient id="paper-tone" x1="0" y1="0" x2="0" y2="1">
      <stop offset="0" stop-color="#ffffff"/>
      <stop offset="1" stop-color="#ececec"/>
    </linearGradient>
    <linearGradient id="blue-field" x1="0" y1="0" x2="0" y2="1">
      <stop offset="0" stop-color="#1466b8"/>
      <stop offset="1" stop-color="#0a4d96"/>
    </linearGradient>
    <linearGradient id="worker-tone" x1="0" y1="0" x2="0" y2="1">
      <stop offset="0" stop-color="#ece9de"/>
      <stop offset="0.4" stop-color="#b69a7e"/>
      <stop offset="1" stop-color="#6d4450"/>
    </linearGradient>
    <linearGradient id="kitchen-before" x1="0" y1="0" x2="1" y2="1">
      <stop offset="0" stop-color="#e9d8bf"/>
      <stop offset="1" stop-color="#b8743e"/>
    </linearGradient>
    <linearGradient id="kitchen-after" x1="0" y1="0" x2="1" y2="1">
      <stop offset="0" stop-color="#8a7868"/>
      <stop offset="1" stop-color="#2e2320"/>
    </linearGradient>
    <clipPath id="before-clip"><circle cx="156" cy="965" r="90"/></clipPath>
    <clipPath id="after-clip"><circle cx="358" cy="994" r="76"/></clipPath>
  </defs>

  <rect class="paper" width="928" height="1300" fill="url(#paper-tone)"/>

  <g role="img" aria-label="Photo: bright renovated apartment with a ladder sketch, two professionals in a hard hat and suit reviewing a clipboard">
    <path d="M0 0 H928 V405 C820 400 650 395 540 370 C420 340 300 300 200 250 C120 210 50 170 0 140 Z" fill="url(#room-tone)"/>
  </g>

  <path class="swoosh" d="M0 150 C70 190 140 240 210 270 L190 300 C120 270 55 230 0 190 Z" fill="var(--brand-blue)"/>
  <path class="swoosh" d="M390 385 C520 420 650 430 790 428 C650 445 520 440 385 410 Z" fill="var(--brand-blue)"/>

  <g class="brand-badge">
    <circle cx="240" cy="337" r="148" fill="#ffffff" stroke="var(--brand-blue)" stroke-width="6"/>
    <text class="brand-name" x="240" y="330" text-anchor="middle">Brightlane</text>
    <text class="brand-name" x="240" y="362" text-anchor="middle">Lending</text>
  </g>

  <text class="headline" x="466" y="577" text-anchor="middle">HARD MONEY FIX &amp;</text>
  <rect class="headline-band" x="160" y="605" width="611" height="80" rx="16" fill="var(--gold)"/>
  <text class="headline-strong" x="466" y="670" text-anchor="middle">FLIP PROGRAMS</text>
  <path d="M220 705 Q465 690 710 705" fill="none" stroke="#dcdcdc" stroke-width="3"/>

  <text class="intro" x="67" y="775">We offer a variety of</text>
  <text class="intro" x="67" y="806">loan programs Some program</text>
  <text class="intro-strong" x="67" y="837">HIGHLIGHTS INCLUDE</text>
  <line x1="297" y1="836" x2="438" y2="836" stroke="var(--text-grey)" stroke-width="1.5"/>

  <g class="highlights">
    <circle cx="497" cy="753" r="4" fill="var(--brand-blue)"/>
    <text class="highlight" x="513" y="760">No Minimum Credit Score, 3-5 Day Close</text>
    <circle cx="497" cy="778" r="4" fill="var(--brand-blue)"/>
    <text class="highlight" x="513" y="785">Up to <tspan class="highlight-accent">100%</tspan> of Purchase &amp; Rehab</text>
    <circle cx="497" cy="803" r="4" fill="var(--brand-blue)"/>
    <text class="highlight" x="513" y="810">Rates as Low as <tspan class="highlight-accent">7%</tspan></text>
    <circle cx="497" cy="829" r="4" fill="var(--brand-blue)"/>
    <text class="highlight" x="513" y="836">Loans Offered Nationwide</text>
  </g>

  <path class="gold-wave" d="M0 945 C200 930 420 960 560 1010 C600 1025 630 1050 660 1085 C560 1040 420 1010 200 1000 C120 998 50 1000 0 1005 Z" fill="var(--gold)"/>
  <path class="blue-field" d="M0 1005 C200 995 420 1010 560 1050 C620 1070 660 1080 690 1095 L690 1300 H0 Z" fill="url(#blue-field)"/>

  <g role="img" aria-label="Photo: smiling contractor in a yellow hard hat and plaid shirt carrying lumber">
    <rect class="worker-photo" x="540" y="905" width="388" height="395" fill="url(#worker-tone)"/>
  </g>

  <g role="img" aria-label="Photo: kitchen before renovation with light wood cabinets">
    <circle cx="156" cy="965" r="95" fill="#ffffff" stroke="var(--gold)" stroke-width="4"/>
    <rect x="60" y="870" width="192" height="190" fill="url(#kitchen-before)" clip-path="url(#before-clip)"/>
  </g>
  <g role="img" aria-label="Photo: kitchen after renovation with dark cabinets and pendant lights">
    <circle cx="358" cy="994" r="81" fill="#ffffff" stroke="var(--gold)" stroke-width="4"/>
    <rect x="280" y="915" width="160" height="160" fill="url(#kitchen-after)" clip-path="url(#after-clip)"/>
  </g>
  <text class="photo-label" x="227" y="1075" text-anchor="middle">Before</text>
  <text class="photo-label" x="411" y="1095" text-anchor="middle">After</text>

  <g class="contact-icons" fill="none" stroke="#ffffff" stroke-width="1.6">
    <path d="M49 1113 c0 8 6 14 14 14 l2 -4 -4 -3 -2 2 c-3 -1 -5 -3 -6 -6 l2 -2 -3 -4 z" fill="#ffffff" stroke="none"/>
    <rect x="48" y="1148" width="16" height="11"/>
    <path d="M48 1148 l8 6 8 -6"/>
    <rect x="50" y="1176" width="12" height="16"/>
    <path d="M53 1181 h6 M53 1185 h6 M53 1189 h4"/>
    <circle cx="56" cy="1214" r="7"/>
    <path d="M49 1214 h14 M56 1207 c-4 4 -4 10 0 14 c4 -4 4 -10 0 -14"/>
  </g>
  <text class="contact-main" x="75" y="1130">(800) 416-2905 x42</text>
  <text class="contact" x="76" y="1160">mvoss@brightlanelending.com</text>
  <text class="contact" x="76" y="1190">NMLS #781536</text>
  <text class="contact" x="76" y="1219">www.brightlanelending.com</text>

  <g class="social" fill="var(--gold)">
    <circle cx="62" cy="1252" r="18"/>
    <circle cx="118" cy="1252" r="18"/>
    <circle cx="171" cy="1252" r="18"/>
  </g>
</svg>
</div>
</body>
</html>
```